Business card design for IT consulting company

Looking for a simple, modern, clean business card design.
Open to reworking our existing logo.

Attached is our current business cards which we do not like.
Ideally double sided with something simple on the back.
Rectangle / Horizonal only.
No rounded edges on the card.
White as the dominate color is preferred.

Target Market(s)

clients, legal, oil & gas, medical, professionals

Industry/Entity Type

IT, tech, consulting

Contact Information for Business Card

Name, Title, email, phone, cell, website

Font styles to use
Sans Serif

Requirements
Must have
• Clean design
Should not have
• loud colors or unusual fonts, etc

```html
<!DOCTYPE html>
<html lang="en">
<head>
<meta charset="utf-8">
<title>Norvale Solutions – Business Card</title>
<link rel="stylesheet" href="https://fonts.googleapis.com/css2?family=Montserrat:wght@500;700&family=Lato:wght@400&family=Inter:wght@700&display=swap">
<style>
  :root {
    --backdrop: #74d3ea;
    --card-white: #ffffff;
    --card-black: #1b1b1b;
    --ink: #2b3544;
    --accent-red: #ef4056;
    --text-dark: #1f1f1f;
    --text-white: #ffffff;
  }
  html, body {
    margin: 0;
    padding: 0;
    width: 1200px;
    height: 1200px;
    overflow: hidden;
    background: var(--backdrop);
  }
  .canvas {
    position: relative;
    width: 1200px;
    height: 1200px;
  }
  .card {
    position: absolute;
    left: 161px;
    width: 878px;
    height: 525px;
    display: block;
  }
  .card--front { top: 41px; }
  .card--back { top: 625px; }
  .name { font-family: "Montserrat", sans-serif; font-size: 36px; }
  .name__first { font-weight: 700; fill: var(--ink); }
  .name__last { font-weight: 500; fill: var(--accent-red); }
  .title { font-family: "Montserrat", sans-serif; font-weight: 500; font-size: 19px; fill: var(--ink); letter-spacing: 0.6px; }
  .contact { font-family: "Lato", sans-serif; font-size: 20px; fill: var(--text-dark); }
  .brand-front { font-family: "Inter", sans-serif; font-weight: 700; font-size: 30px; fill: var(--text-white); }
  .brand-back { font-family: "Inter", sans-serif; font-weight: 700; font-size: 56px; fill: var(--text-white); }
</style>
</head>
<body>
<main class="canvas">

  <!-- Front side -->
  <svg class="card card--front" viewBox="0 0 732 438" xmlns="http://www.w3.org/2000/svg" aria-label="Business card front">
    <rect width="732" height="438" fill="var(--card-white)"/>

    <!-- slanted dark block with a single red rule -->
    <line class="rule-red" x1="372" y1="0" x2="492" y2="438" stroke="var(--accent-red)" stroke-width="4"/>
    <polygon class="panel-dark" points="400,0 732,0 732,438 520,438" fill="var(--card-black)"/>

    <!-- brand name -->
    <text class="brand-front" x="574" y="235" text-anchor="middle">Norvale</text>

    <!-- name and title -->
    <text class="name" x="48" y="82"><tspan class="name__first">Daniel </tspan><tspan class="name__last">Reyes</tspan></text>
    <text class="title" x="48" y="113">IT Consultant</text>
    <rect class="title-rule" x="48" y="131" width="52" height="3" fill="var(--accent-red)"/>

    <!-- contact rows -->
    <g class="contact-row">
      <rect x="48" y="264" width="26" height="26" fill="var(--accent-red)"/>
      <path d="M55 270 q2 -1 4 0 l2 4 q0 2 -2 3 q2 4 6 6 q1 -2 3 -2 l4 2 q1 2 0 4 q-2 2 -5 1 q-10 -4 -13 -13 q-1 -3 1 -5 Z" fill="var(--text-white)"/>
      <text class="contact" x="84" y="284">(555) 201-4410</text>
    </g>
    <g class="contact-row">
      <rect x="48" y="297" width="26" height="26" fill="var(--accent-red)"/>
      <rect x="56" y="301" width="10" height="18" rx="2" fill="none" stroke="var(--text-white)" stroke-width="2"/>
      <circle cx="61" cy="316" r="1.2" fill="var(--text-white)"/>
      <text class="contact" x="84" y="318">(555) 310-7725</text>
    </g>
    <g class="contact-row">
      <rect x="48" y="330" width="26" height="26" fill="var(--accent-red)"/>
      <rect x="53" y="337" width="16" height="12" fill="none" stroke="var(--text-white)" stroke-width="1.6"/>
      <path d="M53 337 L61 344 L69 337" fill="none" stroke="var(--text-white)" stroke-width="1.6"/>
      <text class="contact" x="84" y="350">Daniel.reyes@norvale.ca</text>
    </g>
    <g class="contact-row">
      <rect x="48" y="363" width="26" height="26" fill="var(--accent-red)"/>
      <g fill="none" stroke="var(--text-white)" stroke-width="1.4">
        <circle cx="61" cy="376" r="8"/>
        <ellipse cx="61" cy="376" rx="3.5" ry="8"/>
        <line x1="53" y1="376" x2="69" y2="376"/>
        <line x1="54.5" y1="371.5" x2="67.5" y2="371.5"/>
        <line x1="54.5" y1="380.5" x2="67.5" y2="380.5"/>
      </g>
      <text class="contact" x="84" y="383">www.norvale.ca</text>
    </g>
  </svg>

  <!-- Back side -->
  <svg class="card card--back" viewBox="0 0 732 438" xmlns="http://www.w3.org/2000/svg" aria-label="Business card back">
    <rect width="732" height="438" fill="var(--card-black)"/>
    <rect class="brand-square" x="50" y="169" width="100" height="100" rx="8" fill="var(--accent-red)"/>
    <text class="brand-back" x="172" y="239" textLength="510" lengthAdjust="spacingAndGlyphs">Norvale Solutions</text>
  </svg>

</main>
</body>
</html>
```